Brill Insurance Agency - Business Cards

Hello, I am needing new trendy business cards for our Insurance Agency now that I have a new Logo. I have attached our new logo with several color options along with a business card design that I like. I am leaning towards burgundy and blue colors. I have attached our current business card. I have also attached a headshot of our company president, Martin Vale, that you can use if you wish. Thank you so much in advance for all the wonderful designs!!!!

Target Market(s)

We want to look very professional to potential customers and we also want to look very professional so insurance companies will want to contract with us to sell their product.

Industry/Entity Type

Insurance

Contact Information for Business Card

Martin Vale
mvale@brillagency.com
Business: 555-213-4087
Fax: 555-213-7751
Cell: 555-390-2618
Toll Free: 888-555-0194
42 W Elm Rd Alder Falls, ZZ 00000
www.brillagency.net

Font styles to use
Serif
Sans Serif

Colors
0355a3
3277b5
f04a50
ec1f27

Requirements
Nice to have
• I love creativity. The more creative and balanced a business card design the more I will like it. I would like the card to be printed horizontally instead of vertically.
Should not have
• My project should not have the Allied Coverage Network logo. It is no longer used in the industry.

```html
<!DOCTYPE html>
<html lang="en">
<head>
<meta charset="utf-8">
<title>Brill Insurance Agency – Business Cards</title>
<link rel="stylesheet" href="https://fonts.googleapis.com/css2?family=Source+Sans+3:wght@400;600;700&display=swap">
<style>
  :root {
    --backdrop: #cdd2d1;
    --paper: #fbfbfa;
    --burgundy: #4a0c22;
    --teal: #14a08a;
    --blue: #2f6cb0;
    --ink: #333a3f;
    --divider: #555b60;
  }
  * { box-sizing: border-box; margin: 0; padding: 0; }
  html, body {
    width: 1200px; height: 668px; overflow: hidden;
    background: var(--backdrop);
    font-family: "Source Sans 3", Arial, sans-serif;
  }
  .sheet {
    position: relative; width: 1200px; height: 668px;
    display: flex; align-items: center; justify-content: center; gap: 50px;
  }
  .card {
    position: relative; width: 525px; height: 300px; overflow: hidden;
    box-shadow: 0 10px 24px rgba(0,0,0,.18);
  }
  /* shared brand lockup: one colour, one weight */
  .brand {
    display: flex; align-items: center; gap: 12px;
    color: var(--teal); font-weight: 700; text-transform: uppercase;
    letter-spacing: .5px; line-height: 1.05;
  }
  .brand__dot { border-radius: 50%; background: var(--teal); flex: none; }

  /* front */
  .card--front { background: var(--paper); }
  .front__head {
    position: absolute; left: 150px; top: 30px;
    display: flex; align-items: center; gap: 14px;
  }
  .card--front .brand { font-size: 21px; }
  .card--front .brand__dot { width: 34px; height: 34px; }
  .front__divider { width: 1px; height: 40px; background: var(--divider); }
  .person { position: absolute; left: 30px; top: 104px; }
  .person__name { color: var(--blue); font-weight: 700; font-size: 16px; line-height: 1.2; }
  .person__role { color: var(--teal); font-size: 11px; }
  .rule { position: absolute; left: 30px; right: 30px; top: 148px; height: 1px; background: var(--teal); }
  .contacts {
    position: absolute; left: 30px; right: 30px; top: 160px;
    display: grid; grid-template-columns: 150px 140px 1fr; gap: 12px;
    font-size: 10.5px; color: var(--ink);
  }
  .contacts dl { display: grid; grid-template-columns: max-content 1fr; column-gap: 6px; row-gap: 6px; align-content: start; }
  .contacts dt { color: var(--blue); font-weight: 700; font-size: 11px; line-height: 1.4; }
  .contacts dd { line-height: 1.4; padding-top: 1px; }
  .band {
    position: absolute; left: 0; right: 0; bottom: 0; height: 52px;
    background: var(--burgundy); display: flex; align-items: center; justify-content: flex-end;
    padding-right: 30px;
  }
  .band__web { color: #fff; font-size: 13px; font-weight: 600; letter-spacing: .6px; }

  /* back */
  .card--back { background: var(--burgundy); display: flex; align-items: center; justify-content: center; }
  .card--back .brand { flex-direction: column; font-size: 30px; text-align: center; gap: 14px; }
  .card--back .brand__dot { width: 56px; height: 56px; }
  .back__rule { width: 300px; height: 1px; background: rgba(255,255,255,.25); margin-top: 14px; }
</style>
</head>
<body>
<main class="sheet">
  <section class="card card--front" aria-label="Business card front">
    <div class="front__head">
      <span class="brand__dot" style="width:34px;height:34px;border-radius:50%;background:var(--teal)"></span>
      <span class="front__divider"></span>
      <div class="brand"><span class="brand__text">Brill Insurance<br>Agency Inc</span></div>
    </div>
    <div class="person">
      <p class="person__name">Martin Vale</p>
      <p class="person__role">President</p>
    </div>
    <div class="rule"></div>
    <div class="contacts">
      <dl>
        <dt>Telephone:</dt><dd>888-555-0194</dd>
        <dt>Cellphone:</dt><dd>555-390-2618</dd>
      </dl>
      <dl>
        <dt>Fax:</dt><dd>555-213-7751</dd>
        <dt>Business:</dt><dd>555-213-4087</dd>
      </dl>
      <dl>
        <dt>E-mail:</dt><dd>mvale@brillagency.com</dd>
        <dt>Address:</dt><dd>42 W Elm Rd Alder Falls,<br>ZZ 00000</dd>
      </dl>
    </div>
    <div class="band"><span class="band__web">www.brillagency.net</span></div>
  </section>

  <section class="card card--back" aria-label="Business card back">
    <div class="brand">
      <span class="brand__dot"></span>
      <span class="brand__text">Brill Insurance<br>Agency Inc</span>
      <span class="back__rule"></span>
    </div>
  </section>
</main>
</body>
</html>
```